Lira Vantell Music Flyer for Social Media

The flyer needs to include the networks Lira Vantell music is distributed on such as TuneHarbor, WaveCastFM, Brook, and Soundly. This flyer will be posted on social media websites such as friendloop, Pictogrove, and Chirpnet. The flyer will also be listed on the music artist official website. The artist logo is attached for additional creative ideas.

Target Market(s)

Music lovers

Industry/Entity Type

Music Download

Requirements
Must have
• Must have the music networks listed on the photo and the artist name.
Nice to have
• It would be nice to have the website listed: www.liravantell.example and artist logo.
Should not have
• Anything that is not listed in the project description.

```html
<!DOCTYPE html>
<html lang="en">
<head>
<meta charset="utf-8">
<title>Lira Vantell — Music</title>
<link rel="stylesheet" href="https://fonts.googleapis.com/css2?family=Josefin+Sans:wght@100;300;400;600&display=swap">
<style>
  :root {
    --ink-deep: #07040c;
    --violet-dark: #1c1030;
    --violet-mid: #4a3578;
    --violet-glow: #9c8ad6;
    --neon-pink: #e426d2;
    --neon-pink-soft: #f38cec;
    --name-pink: #cf2dc4;
    --url-violet: #a45fd0;
    --network-white: #f2eef8;
  }
  html, body {
    margin: 0;
    padding: 0;
    width: 848px;
    height: 1200px;
    overflow: hidden;
    background: var(--ink-deep);
  }
  .flyer {
    position: relative;
    width: 848px;
    height: 1200px;
    overflow: hidden;
    font-family: "Josefin Sans", sans-serif;
    background: var(--ink-deep);
  }
  .artist-photo {
    position: absolute;
    inset: 0 0 160px 0;
    background:
      radial-gradient(ellipse 38% 30% at 40% 38%, #8a6aa8 0%, #5b4278 45%, transparent 75%),
      radial-gradient(ellipse 75% 55% at 50% 42%, var(--violet-mid) 0%, var(--violet-dark) 60%, var(--ink-deep) 100%),
      linear-gradient(180deg, #0b0614 0%, #2a1c45 40%, #140b22 80%, var(--ink-deep) 100%);
  }
  .light-flare {
    position: absolute;
    top: 250px;
    width: 260px;
    height: 90px;
    background: radial-gradient(ellipse at center, rgba(220,210,255,0.55) 0%, rgba(180,160,240,0.15) 45%, transparent 70%);
    filter: blur(4px);
  }
  .light-flare--left { left: -90px; transform: rotate(14deg); }
  .light-flare--right { right: -90px; transform: rotate(-14deg); }
  .lower-fade {
    position: absolute;
    left: 0; right: 0; top: 620px; bottom: 0;
    background: linear-gradient(180deg, transparent 0%, rgba(7,4,12,0.7) 35%, var(--ink-deep) 70%);
  }
  .title-art {
    position: absolute;
    left: 0;
    top: 0;
    width: 848px;
    height: 1200px;
  }
  .title-word {
    font-family: "Josefin Sans", sans-serif;
    font-weight: 300;
    fill: none;
    stroke: var(--neon-pink);
    stroke-width: 3;
    filter: drop-shadow(0 0 6px var(--neon-pink)) drop-shadow(0 0 14px rgba(228,38,210,0.6));
  }
  .title-word-core {
    font-family: "Josefin Sans", sans-serif;
    font-weight: 300;
    fill: rgba(243,140,236,0.12);
  }
  .artist-name {
    font-family: "Josefin Sans", sans-serif;
    font-weight: 300;
    fill: var(--name-pink);
    filter: drop-shadow(0 0 4px rgba(207,45,196,0.7));
  }
  .site-url {
    position: absolute;
    left: 0;
    right: 0;
    top: 1093px;
    text-align: center;
    font-weight: 300;
    font-size: 25px;
    letter-spacing: 6px;
    color: var(--url-violet);
  }
  .networks {
    position: absolute;
    left: 120px;
    right: 120px;
    top: 1166px;
    display: flex;
    justify-content: space-between;
    align-items: center;
    margin: 0;
    padding: 0;
    list-style: none;
  }
  .network {
    display: flex;
    align-items: center;
    gap: 6px;
    font-weight: 600;
    font-size: 17px;
    color: var(--network-white);
  }
  .network-dot {
    width: 14px;
    height: 14px;
    border-radius: 50%;
    background: var(--network-white);
  }
</style>
</head>
<body>
  <main class="flyer">
    <div class="artist-photo" role="img" aria-label="Portrait of the smiling artist with voluminous curly hair, lit in violet tones"></div>
    <div class="light-flare light-flare--left"></div>
    <div class="light-flare light-flare--right"></div>
    <div class="lower-fade"></div>

    <svg class="title-art" viewBox="0 0 848 1200" xmlns="http://www.w3.org/2000/svg">
      <text class="title-word-core" x="32" y="984" font-size="410" textLength="792" lengthAdjust="spacingAndGlyphs">MUSIC</text>
      <text class="title-word" x="32" y="984" font-size="410" textLength="792" lengthAdjust="spacingAndGlyphs">MUSIC</text>
      <text class="artist-name" x="32" y="1072" font-size="98" textLength="792" lengthAdjust="spacingAndGlyphs">LIRA VANTELL</text>
    </svg>

    <p class="site-url">www.liravantell.example</p>

    <ul class="networks">
      <li class="network"><span class="network-dot"></span>Soundly</li>
      <li class="network"><span class="network-dot"></span>WaveCastFM</li>
      <li class="network"><span class="network-dot"></span>TuneHarbor</li>
      <li class="network">Brook</li>
    </ul>
  </main>
</body>
</html>
```